Veltamar - Collateral Pocket Envelope and Insert Design

We are looking to have some collateral designed that includes a nice letter size pocket envelope with our logo and then an insert that includes a one-pager about the company. The pocket envelope should be eye-catching but also simple and clean. The insert should include the information we've included under the "Must Have" sections.

Target Market(s)

Entrpreneurs, realtors, lenders, insurance professionals, small business owners, attorneys.

Industry/Entity Type

Business Consultant

Font styles to use
Serif

Colors
f37122
f68d4d
fabb94

Requirements
Must have
• One-page insert should include the following:
• - Company contact info
• - Information about the company and the founders
• - How to get involved? Attend an upcoming meeting. RSVP by sending an email to...
• - What is Veltamar? Who is Veltamar designed for?
• - - Veltamar offers a four-pronged approach:
• o Plan – develop a simple-to-implement and easily executable business plan during our 4 hour workshops either in person or virtually from the comfort of your home or office
• o Be Accountable – report on your progress and initiatives during group meetings and ensure that you are focusing and executing on the activities that truly move the needle
• o Collaborate – engage with like-minded business professionals during our bi-weekly one hour meetings as well as Veltamar member events
• o Grow – enjoy access to an array of articles, videos, discussion boards, and subject matter experts that will help contribute to your professional growth
• o “Through the development of an easy-to-implement and easy-to-execute plan, consistent accountability, a simple score-keeping process, and collaboration with like-minded business professionals, you’ll have the ability to build a better road map to success. "
• o “Rather than develop your plan and turn you loose, Veltamar places heavy emphasis on the importance and value of collaboration and accountability. Veltamar members meet with Veltamar-trained facilitators in a group setting twice a month to review, modify, and update their plans, share challenges and successes, and identify the activities that will truly help ensure they are successful.
• “We assist members in the creation of a simple and easy-to-execute plan that they stay accountable to via our bi-weekly peer collaboration meetings that are facilitated by Veltamar trainers. This approach ensures that members stay focused on and committed to the activities that matter and deliver results.”
• “What Your Membership Includes” which is followed by the following icons/text:
• o Annual Business Plan Creation
• o 24/7/365 Access to your plan dashboard & scoreboard
• o Bi-Weekly Meetings with up 10 other business professionals (hosted by Veltamar trainers)
• o Industry exclusivity
• o Professional Coaching
• o Referral Opportunities
• o Networking Events
• o Utilization of Commonden – Veltamar’s private community education/communication hub

```html
<!DOCTYPE html>
<html lang="en">
<head>
<meta charset="utf-8">
<title>Veltamar – Pocket Folder and Insert</title>
<link rel="stylesheet" href="https://fonts.googleapis.com/css2?family=Open+Sans:wght@400;600;700&display=swap">
<style>
  :root {
    --stage: #e9eaec;
    --folder: #58585a;
    --folder-spine: #4f4f51;
    --orange: #f37122;
    --orange-mid: #f68d4d;
    --orange-soft: #fabb94;
    --ink: #3d3d3f;
    --text: #4a4a4c;
    --white: #ffffff;
    --tag: #4d4d4f;
  }
  * { margin: 0; padding: 0; box-sizing: border-box; }
  html, body { width: 1200px; height: 582px; overflow: hidden; }
  body {
    position: relative;
    background: var(--stage);
    font-family: "Open Sans", Arial, sans-serif;
  }

  /* Pocket folder */
  .folder {
    position: absolute; left: 73px; top: 70px; width: 673px; height: 436px;
    background: var(--folder);
    box-shadow: 0 2px 6px rgba(0,0,0,.25);
  }
  .folder__spine {
    position: absolute; left: 336px; top: 0; width: 14px; height: 100%;
    background: linear-gradient(90deg, var(--folder-spine), var(--folder));
  }
  .folder__brand {
    position: absolute; left: 388px; top: 185px;
    display: flex; align-items: center; gap: 8px;
  }
  .brand-mark { width: 24px; height: 26px; background: var(--orange); }
  .folder__name {
    color: var(--white); font-size: 34px; font-weight: 400; letter-spacing: .5px;
  }
  .folder__contacts { position: absolute; left: 36px; top: 357px; }

  .contact-list { list-style: none; }
  .contact-list li {
    display: flex; align-items: center; gap: 7px;
    color: var(--white); font-size: 11px; height: 19px;
  }
  .contact-icon {
    width: 13px; height: 13px; border-radius: 50%;
    background: var(--orange); display: flex; align-items: center; justify-content: center;
  }
  .contact-icon svg { width: 8px; height: 8px; }

  /* Insert */
  .insert {
    position: absolute; left: 790px; top: 70px; width: 340px; height: 436px;
    background: var(--white); overflow: hidden;
    box-shadow: 0 2px 6px rgba(0,0,0,.25);
  }
  .insert__art { position: absolute; inset: 0; }
  .insert__brand {
    position: absolute; left: 14px; top: 14px;
    display: flex; align-items: center; gap: 5px;
  }
  .insert__brand .brand-mark { width: 14px; height: 16px; }
  .insert__name { color: var(--ink); font-size: 21px; font-weight: 400; }
  .insert__photo {
    position: absolute; left: 0; top: 44px; width: 340px; height: 120px;
    background: linear-gradient(120deg, #c9d3dc 0%, #e8ecef 45%, #9aa6b2 80%, #5a6470 100%);
  }

  .insert__main {
    position: absolute; left: 13px; top: 173px; width: 170px;
    font-size: 5.1px; line-height: 1.32; color: var(--text);
  }
  .insert__lead { color: var(--orange); font-size: 5.5px; text-align: justify; margin-bottom: 6px; }
  .prong h3 { font-size: 6px; font-weight: 700; color: var(--ink); margin-top: 2px; }
  .prong p { margin-bottom: 2px; }

  .insert__side {
    position: absolute; left: 196px; top: 174px; width: 136px;
    color: var(--white); font-size: 4.8px; line-height: 1.32;
  }
  .insert__side p { text-align: justify; margin-bottom: 5px; }
  .membership__title {
    margin: 10px 0 6px -4px; width: 120px;
    background: var(--tag); color: var(--white);
    font-size: 6px; font-weight: 600; padding: 3px 6px;
  }
  .membership__list { list-style: none; }
  .membership__list li {
    display: flex; gap: 5px; align-items: flex-start;
    font-size: 4.9px; line-height: 1.3; min-height: 12.2px;
  }
  .membership__icon {
    flex: none; width: 6px; height: 6px; border-radius: 1px; background: var(--white); margin-top: .5px;
  }
  .insert__contacts { position: absolute; left: 13px; top: 398px; }
  .insert__contacts li { font-size: 7px; height: 12px; gap: 5px; }
  .insert__contacts .contact-icon { width: 9px; height: 9px; }
  .insert__contacts .contact-icon svg { width: 5px; height: 5px; }
</style>
</head>
<body>

<section class="folder" aria-label="Pocket folder cover">
  <div class="folder__spine"></div>
  <div class="folder__brand">
    <span class="brand-mark"></span>
    <span class="folder__name">VELTAMAR</span>
  </div>
  <ul class="contact-list folder__contacts">
    <li><span class="contact-icon"><svg viewBox="0 0 10 10"><path d="M2 1l2 2-1 1.5c.8 1.4 1.8 2.4 3 3L7.5 6l2 2-1.5 1.5C4.5 9 1 5.5.5 2z" fill="#fff"/></svg></span>00000000000</li>
    <li><span class="contact-icon"><svg viewBox="0 0 10 10"><rect x="1" y="2.5" width="8" height="5.5" fill="none" stroke="#fff"/><path d="M1 2.5l4 3 4-3" fill="none" stroke="#fff"/></svg></span>hello@veltamar-mail.com</li>
    <li><span class="contact-icon"><svg viewBox="0 0 10 10"><circle cx="5" cy="5" r="4" fill="none" stroke="#fff"/><path d="M1 5h8M5 1c-2 2.5-2 5.5 0 8M5 1c2 2.5 2 5.5 0 8" fill="none" stroke="#fff" stroke-width=".7"/></svg></span>www.veltamar-group.com</li>
  </ul>
</section>

<section class="insert" aria-label="One-page company insert">
  <svg class="insert__art" viewBox="0 0 340 436" aria-hidden="true">
    <path d="M150 0 H340 V436 H0 V0 Z" fill="none"/>
    <path d="M140 0 H340 V90 C300 40 230 12 140 0 Z" fill="var(--orange-mid)"/>
    <path d="M230 0 C285 12 320 35 340 60 V70 C312 40 275 18 230 0 Z" fill="#8a8a8c"/>
    <rect x="186" y="164" width="154" height="272" fill="var(--orange-mid)"/>
    <path d="M0 164 H194 V400 C130 384 60 370 0 340 Z" fill="var(--white)"/>
    <path d="M0 340 C60 370 130 384 194 400 H340 V436 H0 Z" fill="var(--orange-mid)"/>
    <path d="M0 360 C80 398 200 420 340 422 V436 H0 Z" fill="var(--white)"/>
    <path d="M0 366 C80 404 200 426 340 428 V436 H0 Z" fill="var(--folder)"/>
  </svg>

  <div class="insert__brand">
    <span class="brand-mark"></span>
    <span class="insert__name">VELTAMAR</span>
  </div>

  <div class="insert__photo" role="img" aria-label="Photo of business professionals meeting around a table"></div>

  <div class="insert__main">
    <p class="insert__lead">Through the development of an easy-to-implement and easy-to-execute plan, consistent accountability, a simple score-keeping process, and collaboration with like-minded business professionals, you’ll have the ability to build a better road map to success.</p>
    <div class="prong"><h3>PLAN</h3><p>develop a simple-to-implement and easily executable business plan during our 4 hour workshops either in person or virtually from the comfort of your home or office</p></div>
    <div class="prong"><h3>BE ACCOUNTABLE</h3><p>report on your progress and initiatives during group meetings and ensure that you are focusing and executing on the activities that truly move the needle</p></div>
    <div class="prong"><h3>COLLABORATE</h3><p>engage with like-minded business professionals during our bi-weekly one hour meetings as well as Veltamar member events</p></div>
    <div class="prong"><h3>GROW</h3><p>develop a simple-to-implement and easily executable business plan during our 4 hour workshops either in person or virtually from the comfort of your home or office</p></div>
  </div>

  <div class="insert__side">
    <p>Rather than develop your plan and turn you loose, Veltamar places heavy emphasis on the importance and value of collaboration and accountability. Veltamar members meet with Veltamar-trained facilitators in a group setting twice a month to review, modify, and update their plans, share challenges and successes, and identify the activities that will truly help ensure they are successful.</p>
    <p>We assist members in the creation of a simple and easy-to-execute plan that they stay accountable to via our bi-weekly peer collaboration meetings that are facilitated by Veltamar trainers. This approach ensures that members stay focused on and committed to the activities that matter and deliver results.</p>
    <h2 class="membership__title">WHAT YOUR MEMBERSHIP INCLUDES</h2>
    <ul class="membership__list">
      <li><span class="membership__icon"></span>Annual Business Plan Creation</li>
      <li><span class="membership__icon"></span>24/7/365 Access to your plan dashboard<br>&amp; scoreboard</li>
      <li><span class="membership__icon"></span>Bi-Weekly Meetings with up 10 other business professionals (hosted by Veltamar trainers)</li>
      <li><span class="membership__icon"></span>Industry exclusivity</li>
      <li><span class="membership__icon"></span>Professional Coaching</li>
      <li><span class="membership__icon"></span>Referral Opportunities</li>
      <li><span class="membership__icon"></span>Networking Events</li>
      <li><span class="membership__icon"></span>Utilization of Commonden – Veltamar’s private community education/communication hub</li>
    </ul>
  </div>

  <ul class="contact-list insert__contacts">
    <li><span class="contact-icon"><svg viewBox="0 0 10 10"><path d="M2 1l2 2-1 1.5c.8 1.4 1.8 2.4 3 3L7.5 6l2 2-1.5 1.5C4.5 9 1 5.5.5 2z" fill="#fff"/></svg></span>00000000000</li>
    <li><span class="contact-icon"><svg viewBox="0 0 10 10"><rect x="1" y="2.5" width="8" height="5.5" fill="none" stroke="#fff"/><path d="M1 2.5l4 3 4-3" fill="none" stroke="#fff"/></svg></span>hello@veltamar-mail.com</li>
    <li><span class="contact-icon"><svg viewBox="0 0 10 10"><circle cx="5" cy="5" r="4" fill="none" stroke="#fff"/><path d="M1 5h8" stroke="#fff" stroke-width=".7"/></svg></span>www.veltamar-group.com</li>
  </ul>
</section>

</body>
</html>
```